Financial Advisor Resource Firm needs business card design

Need business card design for company in Omaha NE called Tallowbrook Partners. We provide resources to financial advisors....workshop programs, retirement analysis, and insurance planning. I would like to see designs that use grays, greens, black, and white colors. The final design should communicate 'collaboration' and be simple yet attractive to financial planning clients. I will attached our logo and another picture of a puzzle piece coming together. I would like the incorporate the puzzle picture somehow, maybe on the back somehow, with color or just the gray scale....OR, the picture be the front of the card with 'Tallowbrook' definition on it (see upload) and then company logo, employee name, title, address on the back (see ppt uploaded). The following disclosure needs to be included somewhere- Advisory services offered through Marlowe Ridge Advisors, LLC.
Updates

I uploaded a svg and ai file of the logo

Target Market(s)

Financial planning clients and financial advisors....so pretty diverse age range of about 40-70.

Industry/Entity Type

Financial Planning

Contact Information for Business Card

Dennis K. Holloway, MBA
Founder/President
5727 E. Larkspur Avenue
Suite 418
Omaha, NE 68297
Phone- (402) 555-0147
Cell- (402) 555-0183
Fax- (402) 555-0129
email- dennis@tallowbrookgroup.example
web address- www.tallowbrookgroup.example

Colors
1b1b1b
474747
d3d3d3
ffffff
9bcb3c
abd036

Requirements
Must have
• Must include logo provided, must be 2 sided, and must have disclosure...all of these items listed in project description

```html
<!DOCTYPE html>
<html lang="en">
<head>
<meta charset="utf-8">
<title>Tallowbrook Partners — Business Card</title>
<link href="https://fonts.googleapis.com/css2?family=Roboto:wght@400&family=Work+Sans:wght@400;600&display=swap" rel="stylesheet">
<style>
  :root {
    --ink: #1b1b1b;
    --graphite: #474747;
    --mist: #d3d3d3;
    --paper: #ffffff;
    --leaf: #9bcb3c;
    --lime: #abd036;
    --backdrop: #dedede;
  }
  * { margin: 0; padding: 0; box-sizing: border-box; }
  html, body { width: 1200px; height: 897px; overflow: hidden; }
  body {
    position: relative;
    background: var(--backdrop);
    font-family: "Work Sans", sans-serif;
    color: var(--ink);
  }
  .card {
    position: absolute;
    left: 329px;
    width: 543px;
    height: 310px;
    overflow: hidden;
  }
  .card--front { top: 108px; background: var(--paper); }
  .card--back { top: 479px; background: var(--graphite); }

  .wordmark {
    position: absolute;
    left: 0; right: 0;
    text-align: center;
    font-family: "Work Sans", sans-serif;
    font-weight: 600;
    letter-spacing: 0.5px;
    white-space: nowrap;
  }
  .card--front .wordmark { top: 70px; font-size: 28px; color: var(--ink); }
  .card--back .wordmark { top: 150px; font-size: 30px; color: var(--paper); }

  .identity {
    position: absolute;
    right: calc(543px - 235px);
    top: 175px;
    text-align: right;
  }
  .identity__name {
    font-family: "Roboto", sans-serif;
    font-size: 20px;
    color: var(--leaf);
    line-height: 1;
    white-space: nowrap;
  }
  .identity__title { font-size: 13.5px; margin-top: 7px; }
  .identity__address { font-size: 13.5px; margin-top: 13px; line-height: 19px; white-space: nowrap; }

  .divider {
    position: absolute;
    left: 260px;
    top: 178px;
    width: 1.5px;
    height: 84px;
    background: var(--ink);
  }

  .contacts {
    position: absolute;
    left: 285px;
    top: 174px;
    list-style: none;
    font-size: 13.5px;
    line-height: 19px;
  }
  .contacts li { display: flex; align-items: center; white-space: nowrap; }
  .contacts svg { width: 9px; height: 9px; margin-right: 9px; flex: none; }
  .accent { color: var(--leaf); }

  .disclosure {
    position: absolute;
    left: 0; right: 0;
    bottom: 14px;
    text-align: center;
    font-size: 9px;
    letter-spacing: 0.2px;
    color: var(--graphite);
    white-space: nowrap;
  }

  .backdrop-photo {
    position: absolute;
    inset: 0;
    background:
      radial-gradient(ellipse at 25% 20%, #9a9a9a 0%, transparent 55%),
      radial-gradient(ellipse at 75% 80%, #3a3a3a 0%, transparent 60%),
      linear-gradient(160deg, #8c8c8c 0%, #5e5e5e 50%, #262626 100%);
  }
</style>
</head>
<body>

  <section class="card card--front">
    <div class="wordmark">Tallowbrook Partners</div>

    <div class="identity">
      <p class="identity__name">Dennis K. Holloway, MBA</p>
      <p class="identity__title">Founder/President</p>
      <p class="identity__address">5727 E. Larkspur Avenue<br>Suite 418 Omaha, NE 68297</p>
    </div>

    <div class="divider"></div>

    <ul class="contacts">
      <li>
        <svg viewBox="0 0 10 10" aria-hidden="true"><path d="M2 1 L4 1 L4.5 3 L3.3 4 Q4.5 6 6 6.7 L7 5.5 L9 6 L9 8 Q8.5 9 7.5 9 Q1 8 1 2 Q1 1 2 1 Z" fill="var(--leaf)"/></svg>
        (402) 555-0147
      </li>
      <li>
        <svg viewBox="0 0 10 10" aria-hidden="true"><rect x="2.5" y="0.8" width="5" height="8.4" rx="1" fill="none" stroke="var(--leaf)" stroke-width="1.2"/><circle cx="5" cy="7.6" r="0.6" fill="var(--leaf)"/></svg>
        (402) 555-0183
      </li>
      <li>
        <svg viewBox="0 0 10 10" aria-hidden="true"><rect x="2.5" y="0.5" width="5" height="3" fill="var(--leaf)"/><rect x="0.5" y="3.5" width="9" height="4" rx="1" fill="var(--leaf)"/><rect x="2.5" y="7" width="5" height="2.5" fill="var(--leaf)"/></svg>
        (402) 555-0129
      </li>
      <li>
        <svg viewBox="0 0 10 10" aria-hidden="true"><rect x="0.8" y="2" width="8.4" height="6" fill="none" stroke="var(--leaf)" stroke-width="1"/><path d="M0.8 2 L5 5.5 L9.2 2" fill="none" stroke="var(--leaf)" stroke-width="1"/></svg>
        dennis@tallowbrookgroup.example
      </li>
      <li>
        <svg viewBox="0 0 10 10" aria-hidden="true"><circle cx="5" cy="5" r="4.2" fill="none" stroke="var(--leaf)" stroke-width="0.9"/><ellipse cx="5" cy="5" rx="1.8" ry="4.2" fill="none" stroke="var(--leaf)" stroke-width="0.8"/><path d="M0.8 5 H9.2 M1.6 3 H8.4 M1.6 7 H8.4" stroke="var(--leaf)" stroke-width="0.7"/></svg>
        www.<span class="accent">tallowbrookgroup</span>.example
      </li>
    </ul>

    <p class="disclosure">Advisory services offered through Marlowe Ridge Advisors, LLC.</p>
  </section>

  <section class="card card--back">
    <div class="backdrop-photo" role="img" aria-label="Grayscale photograph of business partners' hands fitting puzzle pieces together"></div>
    <div class="wordmark">Tallowbrook Partners</div>
  </section>

</body>
</html>
```